Book title: Wildflower: The gift of stillness!

This book is called: Wildflower: The gift of stillness!

A guide to understanding the most popular types of coaching and how to find the perfect coach for you.
The coaching industry has exploded over the past few years as the demand for them has increased. With so many different types of coaches it can be intimidating and overwhelming to find the perfect one for you. To further complicate matters, you may experience times in your life when you require multiple coaches. {Book Title} aims to quite the noise and assist you in finding the perfect coach for you. In this book, you will learn more about the different types of coaching as well as meet a hand-picked selection of coaches from the most popular coaching niches. Each featured coach has provided an exercise designed to move you powerfully forward. We encourage you to work through each exercise so you may experience firsthand the power of working with these incredible coaches.

We would like a professional and simple design. See examples included. We would like to see blood orange included in the design, please see color pallets included as well.

Target Market(s)

Corporate professionals wanting to explore the various types of coaching industry

Industry/Entity Type

Coaching - Health, business, spiritual

Font styles to use
Serif

Colors
EE7325
F08F49
F5BC92
FAE3D3
FDF4ED

Requirements
Must have
• Please include book title: Wildflower, Subtitle: The gift of stillness! Name of publishing company: Silver Lantern Publishing, Spaces for 8 author names on the front of the cover- Author Name
Nice to have
• A feminine yet corporate feel.
Should not have
• We don't want it

```html
<!DOCTYPE html>
<html lang="en">
<head>
<meta charset="utf-8">
<title>Wildflower: The gift of stillness!</title>
<link rel="stylesheet" href="https://fonts.googleapis.com/css2?family=Barlow+Condensed:wght@400&family=Barlow:wght@500&family=Montserrat:wght@400&display=swap">
<style>
  :root {
    --page: #ffffff;
    --blood-orange: #f64f0c;
    --petal-peach: #f5a27a;
    --petal-pink: #f48aa0;
    --petal-light: #fad3c0;
    --strip-peach: #f7a585;
    --ink-white: #ffffff;
    --ink-dark: #111111;
  }
  * { margin: 0; padding: 0; box-sizing: border-box; }
  html, body {
    width: 1200px; height: 1200px; overflow: hidden;
    background: var(--page);
  }
  .cover {
    position: absolute;
    left: 242px; top: 63px;
    width: 715px; height: 1074px;
    background: var(--blood-orange);
    overflow: hidden;
  }
  .series-title {
    position: absolute; top: 110px; left: 0; width: 100%;
    text-align: center;
    font-family: "Barlow Condensed", "Arial Narrow", sans-serif;
    font-weight: 400; font-size: 66px; line-height: 1;
    color: var(--ink-white); letter-spacing: 0.01em;
  }
  .main-title {
    position: absolute; top: 178px; left: 0; width: 100%;
    text-align: center;
    font-family: "Barlow Condensed", "Arial Narrow", sans-serif;
    font-weight: 400; font-size: 152px; line-height: 130px;
    color: var(--ink-white); text-transform: uppercase;
  }
  .lotus-art {
    position: absolute; left: 0; top: 403px;
    width: 100%; height: 434px;
    background:
      radial-gradient(ellipse 55% 85% at 50% 100%, #f06a30 0%, #f58a5a 35%, transparent 70%),
      radial-gradient(ellipse 75% 95% at 50% 100%, var(--petal-light) 0%, var(--petal-peach) 45%, var(--petal-pink) 65%, transparent 80%);
  }
  .author-band {
    position: absolute; left: 0; top: 837px;
    width: 100%; height: 134px;
    background: var(--blood-orange);
    display: flex; flex-direction: column; align-items: center; justify-content: center;
    gap: 9px;
  }
  .author-row { display: flex; gap: 10px; }
  .author {
    display: flex; align-items: center; gap: 11px;
    font-family: "Montserrat", Arial, sans-serif;
    font-size: 19px; line-height: 21px;
    color: var(--ink-white);
  }
  .author::before {
    content: ""; width: 12px; height: 12px; border-radius: 50%;
    background: var(--ink-white);
  }
  .publisher-strip {
    position: absolute; left: 0; top: 971px;
    width: 100%; height: 103px;
    background: linear-gradient(180deg, var(--strip-peach), #f8b39a);
  }
  .publisher {
    position: absolute; left: 0; top: 1008px; width: 100%;
    text-align: center;
    font-family: "Barlow", Arial, sans-serif;
    font-weight: 500; font-size: 23px; letter-spacing: 0.32em;
    color: var(--ink-dark); text-transform: uppercase;
  }
</style>
</head>
<body>
  <main class="cover">
    <h1>
      <span class="series-title">WILDFLOWER:</span>
      <span class="main-title">The gift<br>of stillness!</span>
    </h1>
    <div class="lotus-art" role="img" aria-label="Line-art lotus flower with layered peach and pink petals rising from a half sun"></div>
    <section class="author-band">
      <div class="author-row">
        <span class="author">AUTHOR’S NAME</span>
        <span class="author">AUTHOR’S NAME</span>
        <span class="author">AUTHOR’S NAME</span>
      </div>
      <div class="author-row">
        <span class="author">AUTHOR’S NAME</span>
        <span class="author">AUTHOR’S NAME</span>
        <span class="author">AUTHOR’S NAME</span>
      </div>
      <div class="author-row">
        <span class="author">AUTHOR’S NAME</span>
        <span class="author">AUTHOR’S NAME</span>
      </div>
    </section>
    <div class="publisher-strip" role="img" aria-label="Faint reflection of the lotus line-art in soft peach"></div>
    <p class="publisher">Silver Lantern Publishing</p>
  </main>
</body>
</html>
```